New College Graduate Resume - Creative and unique design that stands out from the rest

Need creative resume design for recent college graduate who graduated from School of Music with a concentration in music composition and production. Striving for a contemporary layout/design that allows the resume to "be unique" and "stand out" but be polished and professional. Open to integrating moderate color/graphics as part of resume design but the design can be minus those attributes as well. Attached is raw content in 7 sections (name/contact info, education, highlights of qualifications, work experience, honors/awards, and professional affiliations). While the designer has full latitude over overall design which (section headers, font type, separation/spacing, use of bullets, justification of text, etc.) please maintain current order/sequence of the 7 sections.

Industry/Entity Type

School

Requirements
Must have
• Name (Tobias Hale Whitcombe II) should be most prominent (bold/font size) compared to remainder of resume copy.
• Section headers should be prominent but less so when compared to name on resume.
• The attached file of resume content is provided as raw source copy and is NOT to be just copied and pasted into open fields as is. Expectation is each section of copy will be organized in a manner that is most visually appealing and may include bullets, appropriate spacing, etc.
Should not have
• The attached file of resume content is provided as source copy and is NOT to be just copied and pasted into open fields as is. Expectation is each section of copy will be organized in a manner that

```html
<!DOCTYPE html>
<html lang="en">
<head>
<meta charset="utf-8">
<title>Tobias Hale Whitcombe II – Resume</title>
<link rel="stylesheet" href="https://fonts.googleapis.com/css2?family=Arimo:wght@400;700&display=swap">
<style>
  :root {
    --page: #ffffff;
    --name-bar: #7b7b7b;
    --side-panel: #555555;
    --info-panel: #d9d9d9;
    --ink-light: #ffffff;
    --ink-dark: #333333;
    --ink-mid: #555555;
    --ink-soft: #5f5f5f;
  }
  * { box-sizing: border-box; margin: 0; padding: 0; }
  html, body {
    width: 1000px; height: 1200px; overflow: hidden;
    background: var(--page);
    font-family: "Arimo", Arial, sans-serif;
  }
  .resume { position: relative; width: 1000px; height: 1200px; background: var(--page); overflow: hidden; }

  .studio-banner {
    position: absolute; left: 0; top: 0; width: 1000px; height: 230px;
    background: linear-gradient(100deg, #2a2a2a 0%, #6e6e6e 30%, #3b3b3b 55%, #8a8a8a 75%, #2e2e2e 100%);
  }

  .name-bar {
    position: absolute; left: 19px; top: 254px; width: 74px; height: 912px;
    background: var(--name-bar);
    overflow: hidden;
  }
  .name-bar__inner {
    position: absolute; left: 50%; top: 50%;
    width: 880px; height: 74px;
    transform: translate(-50%, -50%) rotate(-90deg);
    display: flex; flex-direction: column; justify-content: center; align-items: flex-start;
    gap: 6px; padding-left: 18px;
    color: var(--ink-light);
  }
  .name-bar__name { font-weight: 700; font-size: 25px; line-height: 26px; white-space: nowrap; }
  .contact-row { display: flex; gap: 16px; align-items: center; white-space: nowrap; font-size: 12.5px; font-weight: 700; line-height: 14px; }
  .contact-item { display: inline-flex; align-items: center; gap: 6px; }
  .contact-item svg { width: 12px; height: 12px; fill: var(--ink-light); }

  .side-panel {
    position: absolute; left: 106px; top: 254px; width: 335px; height: 912px;
    background: var(--side-panel);
    color: var(--ink-light);
    padding: 52px 28px 0 20px;
    font-size: 15px; line-height: 18.6px;
  }
  .side-heading { font-size: 19px; font-weight: 700; letter-spacing: 0.3px; margin-bottom: 2px; line-height: 21px; }
  .side-section + .side-section { margin-top: 20px; }
  .side-section p { margin: 0; }
  .skill-list { list-style: none; }

  .info-panel {
    position: absolute; left: 448px; width: 523px;
    background: var(--info-panel);
    padding: 0 18px 0 22px;
    color: var(--ink-soft);
  }
  .info-panel--work { top: 254px; height: 654px; padding-top: 18px; }
  .info-panel--honors { top: 922px; height: 122px; padding-top: 14px; }
  .info-panel--affiliation { top: 1057px; height: 109px; padding-top: 14px; }

  .work-heading { font-size: 23px; font-weight: 700; color: var(--ink-dark); line-height: 24px; }
  .panel-heading { font-size: 14.5px; font-weight: 700; color: var(--ink-dark); line-height: 17px; }

  .job + .job { margin-top: 20px; }
  .job__meta { font-size: 13px; font-weight: 700; color: var(--ink-mid); line-height: 16.5px; }
  .job__title { font-size: 15.5px; font-weight: 700; color: var(--ink-mid); line-height: 17px; letter-spacing: 0.2px; }

  .bullet-list { list-style: none; font-size: 12.6px; line-height: 16.6px; }
  .bullet-list li { position: relative; padding-left: 12px; }
  .bullet-list li::before {
    content: ""; position: absolute; left: -2px; top: 6px;
    width: 5px; height: 5px; border-radius: 50%; background: var(--ink-soft);
  }
  .bullet-list .continued::before { display: none; }
  .info-panel--work .bullet-list li { margin-left: -10px; }
  .info-panel--honors .bullet-list, .info-panel--affiliation .bullet-list { font-size: 13.5px; line-height: 17px; color: var(--ink-dark); }
</style>
</head>
<body>
<main class="resume">
  <div class="studio-banner" role="img" aria-label="Black and white photo of hands working a large recording studio mixing console"></div>

  <aside class="name-bar">
    <div class="name-bar__inner">
      <h1 class="name-bar__name">Tobias Hale Whitcombe II</h1>
      <div class="contact-row">
        <span class="contact-item">
          <svg viewBox="0 0 16 16" aria-hidden="true"><path d="M4 1h3l1 4-2 1.5a8 8 0 0 0 3.5 3.5L11 8l4 1v3c0 1-1 2-2 2A12 12 0 0 1 2 3c0-1 1-2 2-2z"/></svg>
          555-214-0386 (cell)
        </span>
        <span class="contact-item">
          <svg viewBox="0 0 16 16" aria-hidden="true"><path d="M1 3h14v10H1zM2 4v.5l6 4.5 6-4.5V4z" fill-rule="evenodd"/></svg>
          thwhitcombe@mailbox.net
        </span>
        <span class="contact-item">
          <svg viewBox="0 0 16 16" aria-hidden="true"><path d="M8 1l7 6h-2v8H9v-5H7v5H3V7H1z"/></svg>
          82 Larkmoor Lane Atlanta, Georgia 30300
        </span>
      </div>
    </div>
  </aside>

  <section class="side-panel">
    <div class="side-section profile">
      <h2 class="side-heading">PROFILE</h2>
      <p>Recent graduate of a highly ranked university seeking opportunities to apply composition and production talents across a variety of music genres and other media.</p>
      <p>Expertise lies in delivering high quality sound design, editing, mixing, and recording.</p>
      <p>Excellent interpersonal skills and the ability to build strong relationships with people at all levels.&nbsp; Exceptionally motivated self-starter and creative problem solver who enjoys working collaboratively on teams.</p>
    </div>
    <div class="side-section education">
      <h2 class="side-heading">EDUCATION</h2>
      <p>Coral Bay University – Linden School of Music</p>
      <p>Coral Springs, Florida</p>
      <p>Bachelor of Music – May 2016</p>
      <p>Major: Media Writing and Production, GPA 3.20/4.0</p>
      <p>Brightwater Academy</p>
      <p>College Park, Georgia</p>
      <p>High School Diploma with Honors – May 2011</p>
    </div>
    <div class="side-section qualifications">
      <h2 class="side-heading">HIGHLIGHTS OF<br>QUALIFICATIONS</h2>
      <ul class="skill-list">
        <li>Media Production Software (SoundDesk 11)</li>
        <li>Sound Design</li>
        <li>Sound Acoustics</li>
        <li>Studio Recording</li>
        <li>Audio Editing</li>
        <li>Audio Mixing</li>
        <li>Analog/Digital board operation</li>
        <li>Music Arranging</li>
        <li>Music Composition</li>
        <li>Music Production</li>
        <li>Composing Sheet Music</li>
        <li>Singer-songwriter</li>
        <li>Rhythm guitarist</li>
      </ul>
    </div>
  </section>

  <section class="info-panel info-panel--work">
    <h2 class="work-heading">WORK EXPERIENCE</h2>
    <article class="job">
      <div class="job__meta">Palmline Film Studio (PFS)<br>Miami, FL<br>May 2014 – Present</div>
      <h3 class="job__title">Sound Engineer</h3>
      <ul class="bullet-list">
        <li>Edited and mixed recorded field audio to professional standards.</li>
        <li>Matched audio with motion picture video to create a seamless product.</li>
        <li>Recorded automated dialogue replacement (ADR) audio and integrated into motion picture video project using SoundDesk 11.</li>
        <li>Recorded foley sound effects to be added to film, video, and other media in post-production.</li>
        <li>Composed and recorded original music to accompany various video projects.</li>
      </ul>
    </article>
    <article class="job">
      <div class="job__meta">Northgate Retail Corporation<br>Atlanta, GA<br>May 2013 - October 2013</div>
      <h3 class="job__title">Sales Associate</h3>
      <ul class="bullet-list">
        <li>Provided customer service, maintained a clean and organized work environment, assisted in sales, and performed cashier responsibilities.</li>
      </ul>
    </article>
    <article class="job">
      <div class="job__meta">Peach State Civic Action Group (PSCAG)<br>Atlanta, GA<br>June 2012 - August 2012</div>
      <h3 class="job__title">On-Site Promoter/Intern</h3>
      <ul class="bullet-list">
        <li>Promoted and advertised various campaigns and managed various office tasks, such as setting up site maps and organizing and sorting non-profit donations.</li>
      </ul>
    </article>
    <article class="job">
      <div class="job__meta">Keystone Direct Sales, Incorporated<br>Atlanta, GA<br>June 2011 – August 2011</div>
      <h3 class="job__title">Product Marketing Consultant</h3>
      <ul class="bullet-list">
        <li>Conducted direct sales and marketing of subsidiary product line through establishing a compelling value proposition, overcoming objections, and closing the sale.</li>
      </ul>
    </article>
  </section>

  <section class="info-panel info-panel--honors">
    <h2 class="panel-heading">HONORS/AWARDS</h2>
    <ul class="bullet-list">
      <li>Best Film and Score: Frights and Frames 2015 Competition (Coral Bay University)</li>
      <li>Harold B Prescott Scholar</li>
      <li>Best New Member, Sigma Rho Delta Fraternity, Inc.</li>
      <li class="continued">Coral Bay University Homecoming King, 2012</li>
    </ul>
  </section>

  <section class="info-panel info-panel--affiliation">
    <h2 class="panel-heading">PROFESSIONAL AFFILIATION</h2>
    <ul class="bullet-list">
      <li>Member, Guild of Composers Incorporated (GCI)</li>
      <li>Member, American Guild of Songwriters, Arrangers, and Publishers (AGSAP)</li>
      <li>Member, Sound Engineering Collective (SEC)</li>
      <li>Member, Sigma Rho Delta Fraternity, Incorporated</li>
    </ul>
  </section>
</main>
</body>
</html>
```